Maple Ridge business card design

Card needs to include the following text/items:
Company Logo
Tobin Marsh
Phone # - 555-318-7642
service@mapleridgelandscaping.example
Lawn & landscape maintenance services

```html
<!DOCTYPE html>
<html lang="en">
<head>
<meta charset="utf-8">
<title>Maple Ridge business card</title>
<link rel="stylesheet" href="https://fonts.googleapis.com/css2?family=Cinzel:wght@400;700&display=swap">
<style>
  :root {
    --backdrop: #262626;
    --card: #ffffff;
    --leaf: #98ab55;
    --forest: #053a1a;
    --forest-edge: #0a4a22;
    --name-blue: #1a86c2;
    --tag-green: #8a9f3e;
  }
  * { margin: 0; padding: 0; box-sizing: border-box; }
  html, body { width: 1200px; height: 900px; overflow: hidden; }
  body {
    background: var(--backdrop);
    font-family: "Cinzel", Georgia, serif;
    position: relative;
  }
  .card {
    position: absolute;
    top: 100px;
    width: 390px;
    height: 700px;
    background: var(--card);
    overflow: hidden;
  }
  .card--front { left: 180px; }
  .card--back { left: 630px; }
  .card__waves {
    position: absolute;
    inset: 0;
    width: 100%;
    height: 100%;
  }
  .brand {
    position: absolute;
    left: 0;
    right: 0;
    display: flex;
    flex-direction: column;
    align-items: center;
  }
  .brand__dot {
    border-radius: 50%;
    background: var(--leaf);
  }
  .brand__name {
    color: var(--forest);
    font-weight: 700;
    text-align: center;
    line-height: 1;
  }
  .card--front .brand { top: 190px; }
  .card--front .brand__dot { width: 200px; height: 200px; margin-bottom: 26px; }
  .card--front .brand__name { font-size: 40px; }
  .card--back .brand { top: 125px; }
  .card--back .brand__dot { width: 150px; height: 150px; margin-bottom: 20px; }
  .card--back .brand__name { font-size: 31px; }
  .contact {
    position: absolute;
    top: 362px;
    left: 0;
    right: 0;
    text-align: center;
    color: var(--name-blue);
  }
  .contact__name { font-size: 27px; font-weight: 400; margin-bottom: 14px; }
  .contact__phone { font-size: 16px; margin-bottom: 6px; }
  .contact__email { font-size: 11.5px; letter-spacing: 0.3px; }
  .tagline {
    position: absolute;
    left: 0;
    right: 0;
    top: 565px;
    text-align: center;
    color: var(--tag-green);
    font-size: 12.5px;
    letter-spacing: 1.6px;
  }
</style>
</head>
<body>

  <article class="card card--front">
    <svg class="card__waves" viewBox="0 0 390 700" preserveAspectRatio="none" aria-hidden="true">
      <path d="M0 0H390V58C320 72 240 50 160 40C90 32 40 44 0 66Z" fill="var(--forest-edge)"/>
      <path d="M0 0H390V50C320 64 240 42 160 32C90 24 40 36 0 58Z" fill="var(--leaf)"/>
      <path d="M0 610C60 640 130 648 210 628C290 608 340 590 390 600V700H0Z" fill="var(--leaf)"/>
      <path d="M0 620C60 650 130 656 210 638C290 620 340 604 390 612V700H0Z" fill="var(--forest)"/>
    </svg>
    <div class="brand">
      <span class="brand__dot"></span>
      <h1 class="brand__name">Maple Ridge</h1>
    </div>
    <p class="tagline">Lawn &amp; landscape maintenance services</p>
  </article>

  <article class="card card--back">
    <svg class="card__waves" viewBox="0 0 390 700" preserveAspectRatio="none" aria-hidden="true">
      <path d="M0 0H390V58C320 72 240 50 160 40C90 32 40 44 0 66Z" fill="var(--forest-edge)"/>
      <path d="M0 0H390V50C320 64 240 42 160 32C90 24 40 36 0 58Z" fill="var(--leaf)"/>
      <path d="M0 610C60 640 130 648 210 628C290 608 340 590 390 600V700H0Z" fill="var(--leaf)"/>
      <path d="M0 620C60 650 130 656 210 638C290 620 340 604 390 612V700H0Z" fill="var(--forest)"/>
    </svg>
    <div class="brand">
      <span class="brand__dot"></span>
      <h2 class="brand__name">Maple Ridge</h2>
    </div>
    <div class="contact">
      <p class="contact__name">Tobin Marsh</p>
      <p class="contact__phone">555-318-7642</p>
      <p class="contact__email">SERVICE@MAPLERIDGELANDSCAPING.EXAMPLE</p>
    </div>
    <p class="tagline">Lawn &amp; landscape maintenance services</p>
  </article>

</body>
</html>
```